Mortgage Broking Flyer to attract attention

We are looking for double sided, colour DL sized flyers for a mail drop to inform people what services we offer.
We are a Mortgage Broking Business in Alice Springs NT Australia. Alice Springs is a large country town so we want something that is personal, a little bit playful but still professional, and is going to capture the attention of potential clients when they first look at it so they want to read on.
Please use our logo and colours (red & white) plus a photo of our team – all attached.
Brochure Front: IMPORTANT
Please come up with a tag line based on the following-We want to be seen as different to the bank, more friendly, personable, we listen, want to help and want people to keep coming back even for the little things.
The home page from our website has good dot points but we would like them shorter and to the point www.ridgecrestlending.com.au
Plus include something which lets customer know that we can assist purchases made through any real estate office, anywhere in Australia
Don’t want the front to contain too many long sentences or paragraphs.
Brochure Back:
Please include:
Services/Specialties
• First home buyers
• Refinancing
• Investments
• Construction loans
• Debt consolidation
• Commercial finance
Please include the following contact details:
Gordon Pell – Managing Director
Maribel Hurst – Loans Consultant
Dana Whitfield – Loans Consultant
Suite 4/17 Corbin Lane, Alice Springs NT 0870
Phone: 08 8914 2718
www.ridgecrestlending.com.au
We must include the following fine print at the back/bottom of the brochure:
Gordon Pell (Credit Representative Number: 572814), Maribel Hurst (Credit Representative Number: 572813) and Dana Whitfield (Credit Representative Number: 630925) are credit representatives of QRVTE Pty Ltd (Australian Credit Licence Number: 648105)
Please feel free to email me with any questions.
dana@ridgecrestlending.com.au

```html
<!DOCTYPE html>
<html lang="en">
<head>
<meta charset="utf-8">
<title>Ridgecrest Lending – DL Flyer Front</title>
<link rel="stylesheet" href="https://fonts.googleapis.com/css2?family=Roboto+Condensed:wght@300;400;700&family=Arimo:wght@700&display=swap">
<style>
  :root {
    --canvas: #eceef0;
    --brand-red: #ec222e;
    --brand-red-deep: #6e0b12;
    --blush: #fdecee;
    --paper: #ffffff;
    --photo-light: #f1f1f1;
    --photo-mid: #c9a9ab;
  }
  html, body {
    margin: 0;
    padding: 0;
    width: 1200px;
    height: 1000px;
    overflow: hidden;
    background: var(--canvas);
  }
  .flyer {
    position: absolute;
    left: 378px;
    top: 35px;
    width: 444px;
    height: 932px;
    background: var(--paper);
    overflow: hidden;
    font-family: "Roboto Condensed", "Arial Narrow", sans-serif;
  }
  .flyer-shapes,
  .hero-photo {
    position: absolute;
    left: 0;
    top: 0;
    width: 444px;
    height: 932px;
  }
  .brand {
    position: absolute;
    left: 35px;
    top: 36px;
    display: flex;
    align-items: center;
    gap: 20px;
  }
  .brand-dot {
    width: 72px;
    height: 72px;
    border-radius: 50%;
    background: var(--paper);
  }
  .brand-name {
    color: var(--paper);
    font-weight: 300;
    font-size: 33px;
    letter-spacing: 0.2px;
    text-transform: uppercase;
  }
  .tagline {
    position: absolute;
    left: 244px;
    top: 178px;
    margin: 0;
    color: var(--paper);
    font-family: "Arimo", Arial, sans-serif;
    font-weight: 700;
    font-size: 21px;
    line-height: 29px;
    text-transform: uppercase;
  }
  .tagline .last { font-size: 23px; }
  .promises {
    position: absolute;
    left: 34px;
    top: 515px;
    margin: 0;
    padding: 0;
    list-style: none;
  }
  .promise {
    display: flex;
    align-items: baseline;
    height: 42.6px;
    color: var(--brand-red);
  }
  .promise-num {
    width: 57px;
    font-weight: 700;
    font-size: 31px;
  }
  .promise-text {
    font-weight: 300;
    font-size: 27px;
    text-transform: uppercase;
  }
  .reach {
    position: absolute;
    left: 28px;
    top: 810px;
    margin: 0;
    color: var(--paper);
    font-weight: 400;
    font-size: 21px;
    line-height: 28px;
    letter-spacing: 0.3px;
  }
  .reach .where { font-size: 25px; line-height: 36px; }
  .reach strong { font-weight: 700; }
</style>
</head>
<body>
  <article class="flyer">
    <svg class="flyer-shapes" viewBox="0 0 444 932" aria-hidden="true">
      <rect class="header-band" x="0" y="0" width="444" height="175" fill="var(--brand-red)"/>
      <polygon class="blush-band-upper" points="0,430 444,455 444,494 0,470" fill="var(--blush)"/>
      <polygon class="blush-band-lower" points="0,728 444,766 444,790 0,790" fill="var(--blush)"/>
      <path class="footer-band" d="M0,932 V828 Q4,782 52,780 L444,768 V932 Z" fill="var(--brand-red)"/>
    </svg>

    <svg class="hero-photo" viewBox="0 0 444 932" role="img" aria-label="Photo of a smiling bearded man in a white shirt holding a small model house, red blurred background">
      <defs>
        <linearGradient id="heroTone" x1="0" y1="0" x2="1" y2="0">
          <stop offset="0" stop-color="var(--photo-light)"/>
          <stop offset="0.45" stop-color="var(--photo-mid)"/>
          <stop offset="0.7" stop-color="var(--brand-red-deep)"/>
          <stop offset="1" stop-color="#a3121b"/>
        </linearGradient>
      </defs>
      <path d="M0,118 Q8,162 60,162 L444,140 V432 Q440,458 404,458 L0,432 Z" fill="url(#heroTone)"/>
    </svg>

    <header class="brand">
      <span class="brand-dot" aria-hidden="true"></span>
      <span class="brand-name">Ridgecrest Lending</span>
    </header>

    <h1 class="tagline">We are<br>different<br><span class="last">from banks</span></h1>

    <ol class="promises">
      <li class="promise"><span class="promise-num">01.</span><span class="promise-text">We are friendly...</span></li>
      <li class="promise"><span class="promise-num">02.</span><span class="promise-text">Personable...</span></li>
      <li class="promise"><span class="promise-num">03.</span><span class="promise-text">We listen...</span></li>
      <li class="promise"><span class="promise-num">04.</span><span class="promise-text">Want to help</span></li>
      <li class="promise"><span class="promise-num">05.</span><span class="promise-text">Want you coming back...</span></li>
    </ol>

    <p class="reach">We can assist purchases made through<br>any real estate office,<br><span class="where">anywhere in <strong>Australia</strong></span></p>
  </article>
</body>
</html>
```